Business Card Design for Marketing Firm

Looking for business card design for higher end marketing firm. Clean but impressionable/trendy. We are a marketing firm that represents manufacturers in the foodservice equipment and supply industry. Our customers are end users such has hotels, restaurants, country clubs, convention centers and casinos as well as distributors of restaurants supplies and equipment, and manufacturers of foodservice equipment and supplies.
Target Market(s)
Hotels, Restaurants, Supply & Equipment Distributors, Foodservice Manufacturers
Industry/Entity Type
Foodservice/Hospitality
Contact Information for Business Card
Name, Title, Contact Number, Email, Website, Social Media, Address
Requirements
Must have
- Clean & Simple but Serious and Impressionable

```html
<!DOCTYPE html>
<html lang="en">
<head>
<meta charset="utf-8">
<title>Calloway Service Group – Business Card</title>
<link href="https://fonts.googleapis.com/css2?family=Cinzel:wght@500&family=Figtree:wght@400;700&display=swap" rel="stylesheet">
<style>
  :root {
    --navy: #010080;
    --white: #ffffff;
    --backdrop: #979797;
  }
  html, body {
    margin: 0;
    padding: 0;
    width: 1200px;
    height: 1200px;
    overflow: hidden;
    background: var(--backdrop);
  }
  .canvas {
    position: relative;
    width: 1200px;
    height: 1200px;
  }
  .card {
    position: absolute;
    top: 175px;
    width: 467px;
    height: 797px;
    overflow: hidden;
  }
  .card-front {
    left: 108px;
    background: var(--white);
    color: var(--navy);
  }
  .card-back {
    left: 624px;
    background: var(--navy);
    color: var(--white);
  }
  .brand-dot {
    position: absolute;
    left: 50%;
    top: 150px;
    width: 64px;
    height: 64px;
    margin-left: -32px;
    border-radius: 50%;
    background: var(--navy);
  }
  .wordmark {
    position: absolute;
    left: 0;
    right: 0;
    top: 253px;
    text-align: center;
    font-family: "Cinzel", serif;
    font-weight: 500;
  }
  .wordmark-main {
    display: block;
    font-size: 29px;
    letter-spacing: 0.5px;
    line-height: 40px;
  }
  .wordmark-rule {
    display: flex;
    align-items: center;
    width: 334px;
    margin: 2px auto 0;
    gap: 10px;
  }
  .wordmark-rule::before {
    content: "";
    flex: 1;
    height: 2px;
    background: var(--navy);
  }
  .wordmark-sub {
    font-size: 17px;
    letter-spacing: 1px;
  }
  .contact {
    position: absolute;
    left: 0;
    right: 0;
    top: 372px;
    text-align: center;
    font-family: "Figtree", sans-serif;
    font-size: 20px;
    line-height: 27px;
  }
  .contact p { margin: 0; }
  .contact .name { font-weight: 700; }
  .contact .gap { margin-top: 26px; }
  .social {
    position: absolute;
    left: 0;
    right: 0;
    top: 734px;
    display: flex;
    justify-content: center;
    gap: 8px;
  }
  .social-dot {
    width: 34px;
    height: 34px;
    border-radius: 50%;
    background: var(--navy);
  }
  .back-name {
    position: absolute;
    left: 0;
    right: 0;
    top: 330px;
    text-align: center;
    font-family: "Cinzel", serif;
    font-weight: 500;
    font-size: 40px;
    line-height: 52px;
    letter-spacing: 1px;
  }
</style>
</head>
<body>
<main class="canvas">
  <section class="card card-front">
    <div class="brand-dot" aria-hidden="true"></div>
    <div class="wordmark">
      <span class="wordmark-main">Calloway Service</span>
      <div class="wordmark-rule"><span class="wordmark-sub">Group</span></div>
    </div>
    <div class="contact">
      <p class="name">Name Surname</p>
      <p>Title</p>
      <p class="gap">123 456 7890</p>
      <p>name@callowayservicegroup.com</p>
      <p>callowayservicegroup.com</p>
      <p class="gap">Larkfield, Nevada</p>
    </div>
    <div class="social" aria-label="Social media">
      <span class="social-dot"></span>
      <span class="social-dot"></span>
    </div>
  </section>
  <section class="card card-back">
    <div class="back-name">Calloway<br>Service<br>Group</div>
  </section>
</main>
</body>
</html>
```